Label design for life altering nutraceutical bottle (60 pills)

We plan to market a form of Vitamin B3 known as nicotinamide riboside (NR) which is found in trace amounts in milk. At higher concentrations this compound can restore aged mitochondria (the energy cells in our bodies) to their youthful levels of activity. NR has the potential to extend years of healthy living and prevent many diseases associated with aging.

We will be selling NR is pill form (375 mg each) with 60 pills per bottle. Our company name is Silverpine Biologics. We need a design for the label to be placed on each pill bottle. The label itself is 19cm x 6cm

Target Market(s)

Health conscious consumers, Longevity, Nerve Pain, High Blood Pressure, Weight Loss

Industry/Entity Type

Nutrition

Logo Text

Silverpine Biologics

Font styles to use
Sans Serif

Colors
ffc214
ffffff

Requirements
Must have
• Language necessary on wraparound bottle label.
• 60 capsules, 375 mg, vegetarian capsule, gluten free, dietary supplement
• WARNING: Do not use if pregnant or nursing. If you are diabetic, have liver disease or stomach ulcers consult your health care practitioner before using this product.
• CAUTION: It is recommended to discontinue use 2 weeks before any elective surgery.
• Keep out of reach of children.
• These statements have not been evaluated by the National Remedy Standards Bureau. This product is not intended to diagnose, treat, cure or prevent any disease.
• US Supplement Facts Label
• "Supplement Facts"
• Serving Size 2 Capsules
• Servings Per Container 30
• Amount Per Serving
• Nicotinamide Riboside 1000mg
• % Daily Value
• 5000%
• Other Ingredients: Vegetable cellulose (capsule)
• Distributed By: Silverpine Biologics LLC, Las Vegas NV, (555) 555-0187, www.SilverpineBiologics.example, Info@SilverpineBiologics.example
Nice to have
• NR (in box in large letters, underneath, the words "Nicotinamide Riboside"
• under box, the words "Turn back the hands of time"
• "New!" in a prominent place on the label.

```html
<!DOCTYPE html>
<html lang="en">
<head>
<meta charset="utf-8">
<title>Nicotinamide Riboside – Bottle Label</title>
<link href="https://fonts.googleapis.com/css2?family=Arimo:wght@400;700&family=Roboto+Condensed:wght@700&display=swap" rel="stylesheet">
<style>
  :root {
    --gold: #ffc214;
    --ink: #111111;
    --paper: #ffffff;
    --backdrop: #ecebe6;
  }
  * { box-sizing: border-box; margin: 0; padding: 0; }
  html, body { width: 1200px; height: 900px; overflow: hidden; }
  body {
    background: var(--backdrop);
    font-family: "Arimo", Arial, sans-serif;
    color: var(--ink);
    position: relative;
  }
  .label {
    position: absolute;
    left: 25px; top: 270px;
    width: 1150px; height: 360px;
    background: var(--paper);
    border-top: 6px solid var(--gold);
    border-bottom: 6px solid var(--gold);
  }
  .divider {
    position: absolute;
    top: 14px; bottom: 14px;
    width: 4px;
    background: var(--gold);
  }
  .divider--first { left: 414px; }
  .divider--second { left: 886px; }

  /* Front panel */
  .front { position: absolute; left: 14px; top: 6px; width: 380px; }
  .product-head { display: flex; align-items: center; height: 118px; }
  .brand-name {
    font-family: "Roboto Condensed", sans-serif;
    font-weight: 700;
    font-size: 30px;
    line-height: 1.05;
    color: var(--gold);
    padding-right: 14px;
    border-right: 2px solid var(--gold);
    height: 104px;
    display: flex; align-items: center;
  }
  .product-name {
    font-family: "Roboto Condensed", sans-serif;
    font-weight: 700;
    font-size: 36px;
    line-height: 1.05;
    color: var(--gold);
    padding-left: 12px;
  }
  .dosage-box {
    margin-top: 8px;
    background: var(--gold);
    border-radius: 5px;
    padding: 7px 12px 6px;
  }
  .dosage-box .count { font-size: 22px; line-height: 1.1; }
  .dosage-box .attributes { font-size: 12.5px; line-height: 1.3; }
  .notice {
    margin-top: 14px;
    font-size: 15px;
    line-height: 1.3;
    text-align: justify;
  }
  .notice b { font-weight: 700; }
  .notice + .notice { margin-top: 22px; }

  /* Facts panel */
  .facts {
    position: absolute;
    left: 442px; top: 12px;
    width: 410px; height: 300px;
    background: var(--gold);
    border-radius: 6px;
    padding: 10px 16px;
    font-size: 15.5px;
    line-height: 1.35;
  }
  .facts .disclaimer { text-align: justify; }
  .facts ul { list-style: none; }
  .facts li::before { content: "\2713\00a0"; }
  .new-burst {
    position: absolute;
    right: 14px; top: 78px;
    width: 150px; height: 116px;
  }
  .keep-away {
    position: absolute;
    left: 442px; width: 410px; top: 320px;
    text-align: center;
    font-size: 17px;
  }

  /* Distributor panel */
  .distributor {
    position: absolute;
    left: 930px; top: 20px;
    height: 310px;
    writing-mode: vertical-rl;
    transform: rotate(180deg);
    text-align: end;
    font-size: 15px;
    line-height: 1.45;
  }
  .distributor .heading { font-weight: 700; font-size: 19px; }
  .distributor .contact { margin-right: 26px; }
  .distributor .contact-line { display: flex; align-items: center; justify-content: flex-end; gap: 6px; }
  .distributor svg { width: 12px; height: 12px; transform: rotate(90deg); }
</style>
</head>
<body>
  <section class="label">
    <div class="front">
      <div class="product-head">
        <div class="brand-name">Silverpine<br>Biologics</div>
        <div class="product-name">Nicotinamide<br>Riboside</div>
      </div>
      <div class="dosage-box">
        <div class="count">60 capsules, 375 mg</div>
        <div class="attributes">vegetarian capsule, gluten free, dietary supplement</div>
      </div>
      <p class="notice"><b>WARNING:</b> Do not use if pregnant or nursing. If you are diabetic, have liver disease or stomach ulcers consult your health care practitioner before using this product.</p>
      <p class="notice"><b>CAUTION:</b> It is recommended to discontinue use 2 weeks before any elective surgery.</p>
    </div>

    <div class="divider divider--first"></div>

    <div class="facts">
      <p class="disclaimer">These statements have not been evaluated by the National Remedy Standards Bureau. This product is not intended to diagnose, treat, cure or prevent any disease.</p>
      <ul>
        <li>US Supplement Facts Label</li>
        <li>"Supplement Facts"</li>
        <li>Serving Size 2 Capsules</li>
        <li>Servings Per Container 30</li>
        <li>Amount Per Serving</li>
        <li>Nicotinamide Riboside 1000mg</li>
        <li>% Daily Value</li>
        <li>5000%</li>
        <li>Other Ingredients: Vegetable cellulose (capsule)</li>
      </ul>
      <svg class="new-burst" viewBox="0 0 150 116" aria-label="New!">
        <polygon fill="#ffffff" points="20,14 48,30 62,4 78,26 104,8 108,34 146,22 126,50 148,66 120,74 130,104 98,86 84,114 70,90 42,106 46,80 6,88 26,62 2,44 30,40"/>
        <text x="76" y="66" text-anchor="middle" font-family="Arimo, Arial, sans-serif" font-size="30" fill="#111">New!</text>
      </svg>
    </div>
    <p class="keep-away">Keep out of reach of children.</p>

    <div class="divider divider--second"></div>

    <div class="distributor">
      <div class="heading">Distributed By:</div>
      <div>Silverpine Biologics LLC</div>
      <div>Las Vegas NV,</div>
      <div class="contact">
        <div class="contact-line"><svg viewBox="0 0 12 12"><path d="M3 1 L5 1 L6 3.5 L4.7 4.6 Q5.6 6.6 7.4 7.3 L8.5 6 L11 7 L11 9 Q10.5 11 8.5 11 Q2 10 1 3.5 Q1 1 3 1Z" fill="#111"/></svg>(555) 555-0187</div>
        <div class="contact-line"><svg viewBox="0 0 12 12"><circle cx="6" cy="6" r="5" fill="none" stroke="#111" stroke-width="1.4"/><ellipse cx="6" cy="6" rx="2" ry="5" fill="none" stroke="#111" stroke-width="1"/><line x1="1" y1="6" x2="11" y2="6" stroke="#111"/></svg>www.SilverpineBiologics.example</div>
        <div class="contact-line"><svg viewBox="0 0 12 12"><rect x="1" y="2.5" width="10" height="7" fill="#111"/><polyline points="1.5,3 6,6.5 10.5,3" fill="none" stroke="#fff"/></svg>Info@SilverpineBiologics.example</div>
      </div>
    </div>
  </section>
</body>
</html>
```